Brookline Wealth Guidance - Employer Benefit Brochure

We need to design a professional looking brochure that we can present to our existing client base, and assist in attracting new clients.
The current information is just provided in a word document, but we need to improve significantly.
The audience would be business leaders, HR decision makers and member policy committee members

Industry/Entity Type

Business

Font styles to use
Sans Serif

Colors
0255a3
f37122

```html
<!DOCTYPE html>
<html lang="en">
<head>
<meta charset="utf-8">
<title>Employer Benefits Partnership – Contents</title>
<link href="https://fonts.googleapis.com/css2?family=Arimo:ital,wght@0,400;0,700;1,700&display=swap" rel="stylesheet">
<style>
  :root {
    --brand-blue: #0255a3;
    --brand-blue-deep: #0a2f86;
    --brand-orange: #f37122;
    --brand-orange-light: #f7923f;
    --ink: #111111;
    --paper: #ffffff;
  }
  html, body { margin: 0; padding: 0; overflow: hidden; }
  body { width: 927px; height: 1200px; background: var(--paper); font-family: "Arimo", Arial, sans-serif; color: var(--ink); }
  .brochure { position: relative; width: 927px; height: 1200px; overflow: hidden; }

  .masthead {
    position: absolute; left: 0; top: 0; width: 927px; height: 92px;
    background: linear-gradient(90deg, var(--brand-blue-deep) 0%, var(--brand-blue) 50%, var(--brand-blue-deep) 100%);
  }
  .masthead-title { position: absolute; left: 42px; top: 26px; margin: 0; font-size: 29px; font-weight: 700; color: #fff; }
  .masthead-divider { position: absolute; left: 498px; top: 20px; width: 2px; height: 48px; background: var(--brand-orange); }
  .masthead-company { position: absolute; left: 512px; top: 27px; font-size: 27px; font-weight: 700; font-style: italic; color: var(--brand-orange); }

  .section-bar {
    position: absolute; left: 0; top: 92px; width: 927px; height: 48px;
    background: linear-gradient(90deg, #e86a1e 0%, var(--brand-orange-light) 55%, var(--brand-orange) 100%);
    color: #fff; font-weight: 700; font-size: 24px;
  }
  .section-bar-title { position: absolute; left: 42px; top: 10px; }
  .section-bar-page { position: absolute; left: 781px; top: 10px; }

  .toc { position: absolute; inset: 0; font-size: 21px; line-height: 26px; }
  .toc div { position: absolute; white-space: nowrap; }
  .toc-program { left: 42px; font-weight: 700; }
  .toc-group { left: 385px; color: var(--brand-orange); }
  .toc-item { left: 385px; }
  .toc-page { left: 800px; }

  .photo-strip { position: absolute; left: 0; top: 996px; width: 927px; height: 116px; background: var(--brand-blue); }
  .photo { position: absolute; top: 7px; height: 109px; }
  .photo-1 { left: 0; width: 217px; background: linear-gradient(135deg, #b8c46a, #d9c9a6 60%, #8fa34f); }
  .photo-2 { left: 224px; width: 179px; background: linear-gradient(135deg, #5fc3e8, #d8b08f 60%, #7fd06b); }
  .photo-3 { left: 409px; width: 165px; background: linear-gradient(135deg, #9fbf6a, #e6e2da 55%, #5f8a3a); }
  .photo-4 { left: 581px; width: 159px; background: linear-gradient(135deg, #e9ebe2, #d8c4a2 55%, #8b8f94); }
  .photo-5 { left: 747px; width: 180px; background: linear-gradient(180deg, #a7bcd0, #dfe6ea 55%, #8a7560); }

  .footer-rule { position: absolute; left: 0; top: 1112px; width: 927px; height: 12px; background: var(--brand-orange); }
  .footer-band {
    position: absolute; left: 0; top: 1124px; width: 927px; height: 76px;
    background: linear-gradient(90deg, var(--brand-blue-deep) 0%, var(--brand-blue) 50%, var(--brand-blue-deep) 100%);
  }
</style>
</head>
<body>
<main class="brochure">
  <header class="masthead">
    <h1 class="masthead-title">Employer Benefits Partnership</h1>
    <span class="masthead-divider"></span>
    <span class="masthead-company">Company Name</span>
  </header>

  <div class="section-bar">
    <span class="section-bar-title">Brookline Financial Services Group</span>
    <span class="section-bar-page">Page</span>
  </div>

  <nav class="toc">
    <div class="toc-program" style="top:162px">Employer Benefits Program:</div>
    <div class="toc-group" style="top:162px">Core Services</div>
    <div class="toc-item" style="top:193px">Corporate Superannuation</div><div class="toc-page" style="top:193px">1</div>
    <div class="toc-item" style="top:224px">Insurance</div><div class="toc-page" style="top:224px">2</div>
    <div class="toc-item" style="top:255px">Financial Literacy &amp; Education</div><div class="toc-page" style="top:255px">3</div>
    <div class="toc-group" style="top:286px">Additional Corporate Services</div>
    <div class="toc-item" style="top:317px">Health Insurance</div><div class="toc-page" style="top:317px">4</div>
    <div class="toc-item" style="top:348px">Travel Insurance</div><div class="toc-page" style="top:348px">4</div>
    <div class="toc-item" style="top:379px">Key Person Insurance</div><div class="toc-page" style="top:379px">5</div>
    <div class="toc-item" style="top:410px">Asset &amp; Equipment Finance</div><div class="toc-page" style="top:410px">5</div>
    <div class="toc-item" style="top:441px">General &amp; Business Insurance</div><div class="toc-page" style="top:441px">5</div>
    <div class="toc-item" style="top:472px">Outplacement Solutions</div><div class="toc-page" style="top:472px">6</div>
    <div class="toc-item" style="top:502px">Professional Contractor Network</div><div class="toc-page" style="top:502px">6</div>

    <div class="toc-program" style="top:577px">Employee Benefits Program:</div>
    <div class="toc-group" style="top:577px">Core Services</div>
    <div class="toc-item" style="top:608px">Superannuation Advice</div><div class="toc-page" style="top:608px">8</div>
    <div class="toc-item" style="top:639px">Insurance Advice</div><div class="toc-page" style="top:639px">9</div>
    <div class="toc-group" style="top:670px">Additional Employee Services</div>
    <div class="toc-item" style="top:701px">Financial Planning</div><div class="toc-page" style="top:701px">10</div>
    <div class="toc-item" style="top:732px">Wills &amp; Estate Planning</div><div class="toc-page" style="top:732px">11</div>
    <div class="toc-item" style="top:763px">Trauma (Critical Illness) Insurance</div><div class="toc-page" style="top:763px">11</div>
    <div class="toc-item" style="top:794px">Home &amp; Investment Lending</div><div class="toc-page" style="top:794px">12</div>
    <div class="toc-item" style="top:825px">Property Advice</div><div class="toc-page" style="top:825px">13</div>
    <div class="toc-item" style="top:855px">Car Leasing Finance</div><div class="toc-page" style="top:855px">13</div>

    <div class="toc-program" style="top:903px">Brookline Fee Flexibility</div><div class="toc-page" style="top:900px">15</div>
    <div class="toc-program" style="top:948px">Brookline Employee Benefits Team</div><div class="toc-page" style="top:946px">17-19</div>
  </nav>

  <section class="photo-strip">
    <div class="photo photo-1" role="img" aria-label="Photo of a smiling retired couple outdoors in a park"></div>
    <div class="photo photo-2" role="img" aria-label="Photo of a laughing couple relaxing on a pool float"></div>
    <div class="photo photo-3" role="img" aria-label="Photo of two older men playing chess on the grass"></div>
    <div class="photo photo-4" role="img" aria-label="Photo of an older couple laughing together on a sofa"></div>
    <div class="photo photo-5" role="img" aria-label="Photo of a retired couple standing on a beach"></div>
  </section>
  <div class="footer-rule"></div>
  <footer class="footer-band"></footer>
</main>
</body>
</html>
```